Business card design Needed for new logo / Construction business, home extensions and new builds

We need a business card design using our new logo files which i will attach to this project :)

We are a small construction business specialising in home extensions, new builds and property development. We are very ambitious and would appreciate professional and elegant designs for our new business card.

Very serious about using the services on BriefNest and recently acquired our new logo from here :)

Please get involved, i will feedback when i can as i am very busy but can respond daily, thanks

Target Market(s)

People that want to build onto their houses, new building developments or adding too their existing property

Industry/Entity Type

Construction

Contact Information for Business Card

Hollin Marsh Construction, Tobias Renwick (Managing Director), Tel 07822200444, email - info@hollin-marsh, www.hollin-marsh.co.uk

Colors

Designer to choose colors to be used in the design.

Requirements
Must have
• I like a deep grey on the back please. A lot of you have provided black from and back, try mixing things up a little. The black looks cool 😎 Thanks

```html
<!DOCTYPE html>
<html lang="en">
<head>
<meta charset="utf-8">
<title>Hollin Marsh Construction – Business Card</title>
<link href="https://fonts.googleapis.com/css2?family=Cinzel:wght@600&family=Open+Sans:wght@400;600;700&display=swap" rel="stylesheet">
<style>
  :root {
    --backdrop: #e9eaec;
    --card-black: #0b0b0b;
    --card-black-soft: #232323;
    --card-grey: #2e2f31;
    --card-grey-soft: #45474a;
    --gold: #e0a526;
    --gold-light: #f6c94f;
    --gold-deep: #a8720f;
    --silver: #c9cbce;
    --silver-light: #f2f3f4;
    --ink: #1a1a1a;
    --text-light: #f1f1f1;
  }
  * { margin: 0; padding: 0; box-sizing: border-box; }
  html, body { width: 818px; height: 1200px; overflow: hidden; }
  body {
    background: var(--backdrop);
    display: flex;
    flex-direction: column;
    align-items: center;
    justify-content: center;
    gap: 110px;
  }
  .card { width: 740px; height: 420px; display: block; filter: drop-shadow(0 10px 18px rgba(0,0,0,.25)); }
  .brand-name { font-family: "Cinzel", serif; font-weight: 600; fill: var(--gold); }
  .contact-text { font-family: "Open Sans", sans-serif; font-weight: 600; fill: var(--text-light); font-size: 19px; }
  .contact-text.small { font-size: 15px; font-weight: 700; }
  .web-pill-text { font-family: "Open Sans", sans-serif; font-weight: 700; fill: var(--ink); font-size: 19px; }
  .holder-name { font-family: "Open Sans", sans-serif; font-weight: 600; fill: var(--ink); font-size: 21px; }
</style>
</head>
<body>

<svg class="card card-front" viewBox="0 0 740 420" aria-label="Business card front">
  <defs>
    <linearGradient id="blackFace" x1="0" y1="0" x2="0" y2="1">
      <stop offset="0" stop-color="var(--card-black-soft)"/>
      <stop offset="1" stop-color="var(--card-black)"/>
    </linearGradient>
    <linearGradient id="goldBand" x1="0" y1="0" x2="1" y2="0">
      <stop offset="0" stop-color="var(--gold-deep)"/>
      <stop offset=".5" stop-color="var(--gold-light)"/>
      <stop offset="1" stop-color="var(--gold)"/>
    </linearGradient>
    <linearGradient id="silverBand" x1="0" y1="0" x2="1" y2="0">
      <stop offset="0" stop-color="var(--silver)"/>
      <stop offset=".5" stop-color="var(--silver-light)"/>
      <stop offset="1" stop-color="var(--silver)"/>
    </linearGradient>
    <clipPath id="frontShape"><rect width="740" height="420" rx="24"/></clipPath>
  </defs>
  <g clip-path="url(#frontShape)">
    <rect class="card-face" width="740" height="420" fill="url(#blackFace)"/>
    <path class="silver-sweep" d="M0 320 Q370 296 740 300 L740 420 L0 420 Z" fill="url(#silverBand)"/>
    <path class="white-sweep" d="M0 334 Q370 312 740 316 L740 420 L0 420 Z" fill="#ffffff"/>
    <path class="gold-sweep" d="M0 392 Q370 376 740 382 L740 420 L0 420 Z" fill="url(#goldBand)"/>
  </g>

  <g class="brand-block">
    <circle cx="370" cy="112" r="34" fill="var(--gold)"/>
    <text class="brand-name" x="370" y="205" text-anchor="middle" font-size="42">HOLLIN MARSH</text>
    <text class="brand-name" x="370" y="240" text-anchor="middle" font-size="21" letter-spacing="4">CONSTRUCTION</text>
  </g>

  <g class="web-pill">
    <rect x="200" y="340" width="340" height="38" rx="19" fill="#ffffff" stroke="var(--gold)" stroke-width="2"/>
    <text class="web-pill-text" x="370" y="366" text-anchor="middle">www.hollin-marsh.co.uk</text>
  </g>
</svg>

<svg class="card card-back" viewBox="0 0 740 420" aria-label="Business card back">
  <defs>
    <linearGradient id="greyFaceBack" x1="0" y1="0" x2="0" y2="1">
      <stop offset="0" stop-color="var(--card-grey-soft)"/>
      <stop offset="1" stop-color="var(--card-grey)"/>
    </linearGradient>
    <linearGradient id="goldBandBack" x1="0" y1="0" x2="1" y2="0">
      <stop offset="0" stop-color="var(--gold-deep)"/>
      <stop offset=".5" stop-color="var(--gold-light)"/>
      <stop offset="1" stop-color="var(--gold)"/>
    </linearGradient>
    <linearGradient id="silverBandBack" x1="0" y1="0" x2="1" y2="0">
      <stop offset="0" stop-color="var(--silver-light)"/>
      <stop offset=".6" stop-color="#ffffff"/>
      <stop offset="1" stop-color="var(--silver)"/>
    </linearGradient>
    <clipPath id="backShape"><rect width="740" height="420" rx="24"/></clipPath>
  </defs>
  <g clip-path="url(#backShape)">
    <rect class="card-face" width="740" height="420" fill="url(#greyFaceBack)"/>
    <path class="silver-band" d="M0 310 Q370 300 740 296 L740 420 L0 420 Z" fill="url(#silverBandBack)"/>
    <path class="gold-band" d="M0 384 Q370 370 740 362 L740 420 L0 420 Z" fill="url(#goldBandBack)"/>
  </g>

  <g class="brand-block">
    <circle cx="170" cy="112" r="32" fill="var(--gold)"/>
    <text class="brand-name" x="170" y="195" text-anchor="middle" font-size="30">HOLLIN MARSH</text>
    <text class="brand-name" x="170" y="224" text-anchor="middle" font-size="16" letter-spacing="3">CONSTRUCTION</text>
  </g>

  <line class="divider" x1="338" y1="60" x2="338" y2="270" stroke="var(--gold)" stroke-width="3"/>

  <g class="contact-list">
    <g class="contact-row phone">
      <circle cx="372" cy="88" r="14" fill="var(--gold)"/>
      <path d="M366 81 l4 -1 2 5 -2 2 q2 4 6 6 l2 -2 5 2 -1 4 q-9 1 -16 -16z" fill="var(--card-black)"/>
      <text class="contact-text" x="398" y="95">07822200444</text>
    </g>
    <g class="contact-row email">
      <circle cx="372" cy="140" r="14" fill="var(--gold)"/>
      <rect x="364" y="134" width="16" height="12" rx="1" fill="none" stroke="var(--card-black)" stroke-width="2"/>
      <path d="M364 135 l8 6 8 -6" fill="none" stroke="var(--card-black)" stroke-width="2"/>
      <text class="contact-text" x="398" y="147">info@hollin-marsh</text>
    </g>
    <g class="contact-row web">
      <circle cx="372" cy="192" r="14" fill="var(--gold)"/>
      <circle cx="372" cy="192" r="8" fill="none" stroke="var(--card-black)" stroke-width="2"/>
      <path d="M364 192 h16 M372 184 v16" stroke="var(--card-black)" stroke-width="1.5"/>
      <text class="contact-text" x="398" y="199">www.hollin-marsh.co.uk</text>
    </g>
    <g class="contact-row company">
      <circle cx="372" cy="242" r="14" fill="var(--gold)"/>
      <rect x="366" y="236" width="12" height="12" fill="var(--card-black)"/>
      <text class="contact-text small" x="398" y="248">Hollin Marsh Construction</text>
    </g>
  </g>

  <g class="card-holder">
    <circle cx="62" cy="338" r="16" fill="var(--gold)"/>
    <circle cx="62" cy="332" r="5" fill="var(--card-black)"/>
    <path d="M53 347 q9 -12 18 0z" fill="var(--card-black)"/>
    <text class="holder-name" x="90" y="345">Tobias Renwick (Managing Director)</text>
  </g>
</svg>

</body>
</html>
```